Tranquilly Balanced Restoration

We want to design a business card that is modern and appealing for an innovative psychedelic telemedicine company that provides at-home ketamine-assisted therapy along with wellness, longevity, and anti-aging medicines. We want to use our deep purple and white plus other colors you can find on our website. We don't have any strict brand guidelines yet so feel free to get creative. We want a very professional, but technology first modern design that will instill trust, peace, calm, but also be attractive to investors in the healthcare and SaaS space.

```html
<!DOCTYPE html>
<html lang="en">
<head>
<meta charset="utf-8">
<title>Tranquilly Balanced Restoration — Business Card</title>
<link href="https://fonts.googleapis.com/css2?family=Marcellus&family=Montserrat:wght@400;600&display=swap" rel="stylesheet">
<style>
  :root {
    --stage: #e9e6ee;
    --card-white: #ffffff;
    --wordmark-pink: #a970a8;
    --brand-purple: #7b64ad;
    --brand-violet: #7d68ae;
    --brand-orchid: #a86aa8;
    --ink: #2b2b2b;
    --on-dark: #ffffff;
  }
  * { margin: 0; padding: 0; box-sizing: border-box; }
  html, body { width: 900px; height: 1200px; overflow: hidden; }
  body {
    background: var(--stage);
    position: relative;
    font-family: "Montserrat", Arial, sans-serif;
  }
  .card {
    position: absolute;
    left: 80px;
    width: 742px;
    height: 440px;
    border-radius: 36px;
    overflow: hidden;
  }
  .card--front { top: 132px; background: var(--card-white); }
  .card--back {
    top: 638px;
    background: linear-gradient(90deg, var(--brand-violet) 0%, var(--brand-orchid) 100%);
  }
  .wordmark {
    position: absolute;
    font-family: "Marcellus", Georgia, serif;
    font-weight: 400;
    line-height: 1;
    white-space: nowrap;
  }
  .card--front .wordmark {
    left: 48px; top: 50px;
    font-size: 66px;
    color: var(--wordmark-pink);
  }
  .brand-dot { position: absolute; border-radius: 50%; }
  .card--front .brand-dot {
    left: 450px; top: 110px; width: 210px; height: 210px;
    background: var(--brand-purple);
  }
  .person { position: absolute; left: 43px; top: 176px; }
  .person__name {
    font-size: 25px; font-weight: 600; color: var(--brand-purple);
  }
  .person__role { font-size: 16px; color: var(--ink); margin-top: 2px; }
  .address {
    position: absolute; left: 48px; top: 255px;
    font-size: 16px; line-height: 20px; color: var(--ink);
  }
  .contact {
    position: absolute; left: 44px; top: 324px;
    list-style: none; font-size: 16px; line-height: 21px; color: var(--ink);
  }
  .contact li { display: flex; align-items: center; gap: 9px; }
  .contact svg { width: 15px; height: 15px; fill: var(--brand-purple); flex: none; }
  .card--back .brand-dot {
    left: 320px; top: 78px; width: 102px; height: 102px;
    background: var(--on-dark);
  }
  .card--back .wordmark {
    left: 0; right: 0; top: 302px; text-align: center;
    font-size: 64px; color: var(--on-dark);
  }
</style>
</head>
<body>
  <section class="card card--front">
    <div class="wordmark">Tranquilly</div>
    <div class="brand-dot"></div>
    <div class="person">
      <div class="person__name">Selena Aldervik</div>
      <div class="person__role">Co-Founder</div>
    </div>
    <div class="address">
      <div>Lindenweg 42</div>
      <div>20457 Hamburg</div>
    </div>
    <ul class="contact">
      <li>
        <svg viewBox="0 0 16 16" aria-hidden="true"><path d="M2 6c0-2 3-3 6-3s6 1 6 3v1h-3V6H5v1H2z"/><rect x="3" y="8" width="10" height="6" rx="1"/></svg>
        833-555-0192
      </li>
      <li>
        <svg viewBox="0 0 16 16" aria-hidden="true"><path d="M1 4h14v1l-7 4-7-4z"/><path d="M1 6.5l7 4 7-4V12H1z"/></svg>
        hello@tranquilly.com
      </li>
      <li>
        <svg viewBox="0 0 16 16" aria-hidden="true"><circle cx="8" cy="8" r="7"/></svg>
        www.tranquilly.com
      </li>
    </ul>
  </section>

  <section class="card card--back">
    <div class="brand-dot"></div>
    <div class="wordmark">Tranquilly</div>
  </section>
</body>
</html>
```